Sales Flyer for Outdoor Kitchens

Looks to have a trifold flyer designed based off website content / projects. Use www.brickleafyardworks.com for content

```html
<!DOCTYPE html>
<html lang="en">
<head>
<meta charset="utf-8">
<title>Brickleaf Yardworks – Outdoor Kitchens Trifold</title>
<link href="https://fonts.googleapis.com/css2?family=Montserrat:wght@400;500;600;700&family=Oswald:wght@500;600&display=swap" rel="stylesheet">
<style>
  :root {
    --green: #3cb54a;
    --green-dark: #2e9a3b;
    --blue: #1a75bb;
    --ink: #2b2b2b;
    --paper: #ffffff;
    --backdrop: #eceeec;
    --photo-sky: #8fb6d8;
    --photo-stone: #b9ab92;
    --photo-wood: #8a5a35;
    --photo-steel: #a7abae;
    --photo-lawn: #6f9a4e;
  }
  * { box-sizing: border-box; margin: 0; padding: 0; }
  html, body { width: 1200px; height: 615px; overflow: hidden; }
  body {
    background: var(--backdrop);
    font-family: "Montserrat", Arial, sans-serif;
    color: var(--ink);
    position: relative;
  }
  .sheet {
    position: absolute;
    top: 101px;
    width: 585px;
    height: 412px;
    background: var(--paper);
    display: flex;
    overflow: hidden;
    box-shadow: 0 10px 18px rgba(0,0,0,.22);
  }
  .sheet--outside { left: 10px; }
  .sheet--inside { left: 605px; }
  .panel { position: relative; width: 195px; height: 100%; padding: 14px 12px 0; }
  .panel--green { background: var(--green); color: #fff; }
  .panel--cover { background: linear-gradient(90deg, #e7e8e8 0%, #ffffff 35%, #ffffff 100%); }

  .heading-blue { color: var(--blue); font-weight: 600; font-size: 11.5px; line-height: 1.15; text-transform: uppercase; }
  .subhead { color: var(--green); font-weight: 600; font-size: 7px; text-transform: uppercase; margin-top: 8px; }
  .heading-green { color: var(--green); font-weight: 600; font-size: 8px; text-transform: uppercase; line-height: 1.15; }
  .heading-white { color: #fff; font-weight: 600; font-size: 7.6px; line-height: 1.2; }
  .body { font-size: 4.9px; line-height: 1.42; margin-top: 3px; text-align: justify; }
  .panel--green .body { color: #fff; }

  .photo { border-radius: 4px; }
  .photo--pavilion { background: linear-gradient(180deg, var(--photo-sky) 0%, var(--photo-wood) 45%, var(--photo-lawn) 100%); }
  .photo--kitchen { background: linear-gradient(180deg, #d9d8d4 0%, var(--photo-stone) 55%, #7b7466 100%); }
  .photo--steel { background: linear-gradient(160deg, #cfd3d6 0%, var(--photo-steel) 50%, #6c7073 100%); }
  .photo--pool { background: linear-gradient(180deg, var(--photo-lawn) 0%, #8a9a86 55%, #4fb3d8 100%); }
  .photo--fire { background: radial-gradient(circle at 45% 55%, #f0a640 0%, #8a6a45 30%, #4b5b3b 100%); }

  .ring {
    position: absolute;
    border-radius: 50%;
    border: 4px solid var(--green);
    box-shadow: 0 4px 0 0 var(--blue);
  }

  /* outside */
  .about-title { text-align: center; font-size: 11px; font-weight: 500; letter-spacing: .5px; margin-top: 6px; }
  .about-copy { text-align: center; }
  .about-copy .body { text-align: justify; margin-top: 7px; }
  .contact { position: absolute; left: 0; right: 0; text-align: center; color: #fff; }
  .contact__address { top: 328px; font-size: 6.2px; line-height: 1.3; }
  .contact__phone { top: 340px; font-family: "Oswald", Arial, sans-serif; font-weight: 500; font-size: 26px; letter-spacing: .3px; }
  .contact__email { top: 380px; font-size: 6.6px; }

  .brand { position: absolute; top: 250px; left: 0; right: 0; display: flex; align-items: center; justify-content: center; gap: 6px; }
  .brand__dot { width: 14px; height: 14px; border-radius: 50%; background: var(--green); }
  .brand__name { color: var(--blue); font-weight: 600; font-size: 11px; text-transform: uppercase; letter-spacing: .3px; }
  .tagline { position: absolute; top: 316px; left: 0; right: 0; text-align: center; font-family: "Oswald", Arial, sans-serif; line-height: 1; }
  .tagline__small { color: var(--green-dark); font-size: 17px; font-weight: 500; display: block; }
  .tagline__big { color: var(--blue); font-size: 34px; font-weight: 600; display: block; margin: 2px 0; }

  /* inside */
  .checklist { list-style: none; margin-top: 10px; }
  .checklist li { display: flex; gap: 5px; font-size: 4.9px; line-height: 1.42; margin-bottom: 6px; }
  .checklist svg { flex: none; width: 7px; height: 7px; margin-top: 1px; }
  .note { color: var(--blue); font-size: 4.9px; line-height: 1.4; font-weight: 600; margin-top: 10px; }
  .note span { font-weight: 400; display: block; }
  .photo-pair { display: flex; gap: 7px; margin-top: 6px; }
  .photo-pair .photo { flex: 1; height: 82px; }
  .spaced { margin-top: 14px; }
</style>
</head>
<body>

<!-- Outside of the trifold -->
<section class="sheet sheet--outside">
  <div class="panel">
    <h2 class="heading-blue">Effective Process<br>for Great Outcomes</h2>
    <h3 class="subhead">Tell us about your project</h3>
    <p class="body">This is where you can share your ideas of your dream backyard with us. The more detail you provide the better prepared we can be for the next step but in just a few minutes you can be on your way to a new dream backyard!</p>
    <h3 class="subhead">Phone consultation</h3>
    <p class="body">Upon review of your project information plan, we will give you a call to discuss your plans, budgets &amp; timelines. If you choose to proceed, then we will discuss timing of step 3.</p>
    <h3 class="subhead">In-person consultation</h3>
    <p class="body">We will visit you at your location and walk through your space to better understand your visions. This is a good time for an initial assessment of project challenges and options to be considered in the next step.</p>
    <div class="ring photo--kitchen" style="left:-12px;top:190px;width:148px;height:148px" role="img" aria-label="Photo of a stone outdoor kitchen with grill doors"></div>
    <div class="ring photo--pavilion" style="left:62px;top:298px;width:116px;height:116px" role="img" aria-label="Photo of a white covered patio with seating"></div>
  </div>

  <div class="panel panel--green">
    <h2 class="about-title">ABOUT US</h2>
    <div class="about-copy">
      <p class="body">Brickleaf Yardworks plans and builds outdoor kitchens, pavilions and living spaces across the greater Houston area. We guide every project from first sketch to final walkthrough, handling design, permits and construction so homeowners can enjoy a finished backyard without juggling separate trades or schedules.</p>
      <p class="body">Our team combines careful planning with quality materials such as natural stone, stainless steel appliances and hand-finished timber. Each build is shaped around the way your family cooks, gathers and relaxes, with layouts that make the most of shade, views and the flow between the house and the yard.</p>
      <p class="body">We keep you informed at every stage and deliver a space built to last for years of outdoor living.</p>
    </div>
    <div class="photo photo--pavilion" style="position:absolute;left:21px;top:212px;width:154px;height:102px;border-radius:0" role="img" aria-label="Photo of a cedar pavilion over a patio with lounge seating"></div>
    <p class="contact contact__address">4820 Meadow Bend Rd Ste 210<br>Riverton, 77512, US</p>
    <p class="contact contact__phone">555-014-7290</p>
    <p class="contact contact__email">rb@brickleafyardworks.com</p>
  </div>

  <div class="panel panel--cover">
    <div class="brand"><span class="brand__dot"></span><span class="brand__name">Brickleaf Yardworks</span></div>
    <h1 class="tagline">
      <span class="tagline__small">CREATE</span>
      <span class="tagline__big">YOUR DREAM</span>
      <span class="tagline__small">BACKYARD WITH US</span>
    </h1>
  </div>
</section>

<!-- Inside of the trifold -->
<section class="sheet sheet--inside">
  <div class="panel">
    <h2 class="heading-green">Design</h2>
    <p class="body">The majority of HOA &amp; municipalities in our area require at least a conceptual plan and construction drawings. We offer an independently contracted design phase for this portion of a project. Design contracts range from $1,500 to $5,000 depending on HOA requirements. In this phase, we will develop:</p>
    <ul class="checklist">
      <li><svg viewBox="0 0 10 10"><circle cx="5" cy="5" r="4.2" fill="none" stroke="#1a75bb" stroke-width="1.2"/><path d="M2.8 5.2l1.6 1.6 3.2-3.4" fill="none" stroke="#1a75bb" stroke-width="1.3"/></svg><span>Master plan which will layout the basic concept / design in your space</span></li>
      <li><svg viewBox="0 0 10 10"><circle cx="5" cy="5" r="4.2" fill="none" stroke="#1a75bb" stroke-width="1.2"/><path d="M2.8 5.2l1.6 1.6 3.2-3.4" fill="none" stroke="#1a75bb" stroke-width="1.3"/></svg><span>3D Model pictures &amp; videos will provide an excellent way for you to visualize your space and its functionality.</span></li>
      <li><svg viewBox="0 0 10 10"><circle cx="5" cy="5" r="4.2" fill="none" stroke="#1a75bb" stroke-width="1.2"/><path d="M2.8 5.2l1.6 1.6 3.2-3.4" fill="none" stroke="#1a75bb" stroke-width="1.3"/></svg><span>After the architectural elements of the design are locked, we will utilize a Texas registered engineer to develop the required construction drawings to support HOA approval &amp; permits.</span></li>
      <li><svg viewBox="0 0 10 10"><circle cx="5" cy="5" r="4.2" fill="none" stroke="#1a75bb" stroke-width="1.2"/><path d="M2.8 5.2l1.6 1.6 3.2-3.4" fill="none" stroke="#1a75bb" stroke-width="1.3"/></svg><span>We will provide cost analysis of decisions throughout the design process but at the end of the phase, you will also receive a construction proposal from Brickleaf.</span></li>
    </ul>
    <p class="note">Note:<span>all design documents &amp; drawings are owned by you upon full payment for design.</span></p>
    <h2 class="heading-green spaced">Aliana Outdoor Kitchen Addition</h2>
    <p class="body">The majority of HOA &amp; municipalities in our area require at least a conceptual plan and construction drawings. We offer an independently contracted design phase for this portion of a project. Design contracts range from $1,500 to $5,000 depending on HOA requirements. In this phase, we will develop:</p>
    <div class="photo-pair">
      <div class="photo photo--kitchen" role="img" aria-label="Photo of a stone grill island on a patio"></div>
      <div class="photo photo--kitchen" role="img" aria-label="Photo of a stacked stone kitchen wall beside the house"></div>
    </div>
    <p class="body" style="margin-top:12px">Every outdoor kitchen we build starts with a conversation about how you want to use the space. From compact grill stations to full covered kitchens, we tailor each plan to your yard, your budget and your style.</p>
  </div>

  <div class="panel panel--green">
    <h2 class="heading-white">Freestanding Pavilion &amp; Kitchen<br>In Richmond, TX</h2>
    <p class="body">This stunning outdoor pavilion with professional kitchen, features a 3-sided gable structure, hand sanded and stained Douglas Fir beams and ceiling, poured in place concrete countertops, professional range, built in Ridgeway pellet grill and stainless-steel griddle. A few other highlights include built in commercial rinse station, Ridgeway stainless steel doors, drawers and dry pantry, built in stainless ice chest, 3 door under counter refrigerator and a matching coffee table with a built-in fire feature!</p>
    <div class="photo-pair">
      <div class="photo photo--pavilion" role="img" aria-label="Photo of a pavilion kitchen under a timber ceiling"></div>
      <div class="photo photo--pavilion" role="img" aria-label="Photo of a pavilion dining table with slatted wall"></div>
    </div>
    <h2 class="heading-white" style="margin-top:8px">Woodlands Freestanding<br>Pavilion &amp; Kitchen</h2>
    <p class="body">This gorgeous kitchen features Austin Stone, quartzite counter tops, stamped concrete, top of the line Larkfield Home appliances, recessed lighting and gas lanterns. It was important to bring our clients style from inside of their home out. Our clients will be able to entertain and relax in these spaces all year long!</p>
    <div class="photo-pair">
      <div class="photo photo--pavilion" role="img" aria-label="Photo of a white gable pavilion with bar seating"></div>
      <div class="photo photo--pool" role="img" aria-label="Photo of a pavilion beside a swimming pool"></div>
    </div>
    <p class="body" style="margin-top:8px">Whether you are adding a simple grill island or a full pavilion with fireplace, television wall and bar seating, our crews treat your property with care. We coordinate deliveries, inspections and clean-up so the work stays on schedule, and we walk through every detail with you before the project is complete.</p>
  </div>

  <div class="panel">
    <h2 class="heading-green">Sugarland Outdoor<br>Kitchen Addition</h2>
    <p class="body">Kitchen build-out of an existing covered patio. This beautiful space was finished with Austin stone, Ridgeway appliances and doors, natural stone counter tops and a gorgeous concrete overlay.</p>
    <div class="photo-pair">
      <div class="photo photo--kitchen" role="img" aria-label="Photo of a covered patio kitchen with stone counters"></div>
      <div class="photo photo--steel" role="img" aria-label="Photo of a stainless steel built-in grill"></div>
    </div>
    <div class="ring photo--steel" style="left:44px;top:188px;width:166px;height:166px" role="img" aria-label="Photo of a stainless grill and doors set in brick"></div>
    <div class="ring photo--fire" style="left:12px;top:308px;width:108px;height:108px" role="img" aria-label="Photo of a lit stone fire pit at dusk"></div>
  </div>
</section>

</body>
</html>
```